Corvane

I'm looking for business cards with the logo I've attached. I don't have an specific idea in mind and open to anything. All the usual info will be involved. Name, position in company, nr, email, address

```html
<!DOCTYPE html>
<html lang="en">
<head>
<meta charset="utf-8">
<title>Corvane Business Cards</title>
<link rel="stylesheet" href="https://fonts.googleapis.com/css2?family=Cabin:wght@400;600&display=swap">
<style>
  :root {
    --navy: #1b2f4e;
    --gold: #ecb03d;
    --white: #ffffff;
    --paper: #ffffff;
    --muted: #c9d1de;
    --shadow: rgba(0, 0, 0, 0.18);
    --edge: #dddddd;
  }
  html, body {
    margin: 0;
    padding: 0;
    width: 1200px;
    height: 1200px;
    overflow: hidden;
    background: var(--paper);
  }
  .sheet {
    position: relative;
    width: 1200px;
    height: 1200px;
  }
  .card {
    position: absolute;
    width: 435px;
    height: 249px;
    background: var(--navy);
    box-shadow: 5px 5px 4px var(--shadow);
    overflow: hidden;
    font-family: "Cabin", sans-serif;
    font-weight: 600;
  }
  .card--contact      { left: 122px; top: 300px; }
  .card--front-light  { left: 612px; top: 300px; background: var(--white); box-shadow: 0 0 0 1px var(--edge), 6px 6px 4px var(--shadow); }
  .card--back-gold    { left: 122px; top: 621px; }
  .card--front-dark   { left: 612px; top: 621px; }

  .corner-art {
    position: absolute;
    right: 0;
    bottom: 0;
    width: 200px;
    height: 170px;
  }
  .corner-art--white { background: linear-gradient(to top left, rgba(255,255,255,0.55), rgba(255,255,255,0) 75%); }
  .corner-art--gold  { background: linear-gradient(to top left, rgba(236,176,61,0.8), rgba(236,176,61,0) 75%); }

  .corner-name {
    position: absolute;
    left: 26px;
    top: 16px;
    margin: 0;
    font-size: 27px;
    letter-spacing: 0.5px;
    line-height: 1.2;
    color: var(--gold);
  }

  .contact {
    position: absolute;
    left: 26px;
    top: 24px;
    width: 200px;
    color: var(--white);
    font-weight: 400;
    font-size: 12px;
    line-height: 1.6;
  }
  .contact__name {
    margin: 0;
    font-weight: 600;
    font-size: 17px;
    line-height: 1.2;
    color: var(--gold);
  }
  .contact__role {
    margin: 2px 0 14px;
    font-size: 11px;
    letter-spacing: 1.5px;
    text-transform: uppercase;
    color: var(--muted);
  }
  .contact__line { margin: 0; }

  .brand {
    position: absolute;
    left: 0;
    right: 0;
    top: 108px;
    display: flex;
    align-items: center;
    justify-content: center;
    gap: 12px;
  }
  .brand__mark {
    width: 20px;
    height: 20px;
    background: var(--navy);
  }
  .card--front-dark .brand__mark { background: var(--white); }
  .brand__name {
    margin: 0;
    font-size: 27px;
    letter-spacing: 0.5px;
    line-height: 1.2;
    color: var(--gold);
  }
</style>
</head>
<body>
<main class="sheet">
  <section class="card card--contact">
    <div class="contact">
      <p class="contact__name">Elena Marsh</p>
      <p class="contact__role">Creative Director</p>
      <p class="contact__line">+1 555 014 2290</p>
      <p class="contact__line">elena@corvane.co</p>
      <p class="contact__line">48 Alder Row, Portland, OR</p>
    </div>
    <div class="corner-art corner-art--white" role="img" aria-label="White mountain line illustration in the lower right corner"></div>
  </section>

  <section class="card card--front-light">
    <div class="brand">
      <span class="brand__mark"></span>
      <p class="brand__name">CORVANE</p>
    </div>
  </section>

  <section class="card card--back-gold">
    <p class="corner-name">CORVANE</p>
    <div class="corner-art corner-art--gold" role="img" aria-label="Gold mountain line illustration in the lower right corner"></div>
  </section>

  <section class="card card--front-dark">
    <div class="brand">
      <span class="brand__mark"></span>
      <p class="brand__name">CORVANE</p>
    </div>
  </section>
</main>
</body>
</html>
```